BrightPlacely.com Wordpress Theme

Hi,

I am looking for a new theme for my wordpress site. The site looks average at the moment and needs a boost. I want to have a better user experience for publishers and advertisers and the proposition for each needs to be clear with better links to registration for both.

Publisher and Advertiser sign up buttons should be on the home page.

I am leaving the brief open save I request that you use green colours on the template.

I want room to be able to add more tabs on the top level if we introduce a blog or other services.

The layout needs to be solid and please work with the copy that's already there.

see http://brightplacely.example

I am looking forward to reviewing your ideas and designs.
Updates

The button to carbon neutral cert I am going to want to make smaller and put it in the bottom of the site.

Do not go down the too fluffy green route with windmills and fuzzy clouds. I am looking for something simple, professional but also organic with a bit of zest to it. 

We are not a niche player serving ads to green only site with green only ads. We simply neutralise the effect of online advertising campaigns.

Some decent images in the header on rotation could work I am not sure. I think these would have to be abstract and largely if not totally green in colour.

Target Market(s)

BrightPlacely.com is an online ad network. Our targets are publishers and advertisers. We bring them together through providing ad serving to the network we have built on behalf of our advertisers.

Advertisers are agencys, brands, large companies looking to sell online or create awareness of the brand.

Requirements
Must have
• Please keep the site clean and use green and white
• Call to action to both publishers and advertisers to join (buttons on home page)

```html
<!DOCTYPE html>
<html lang="en">
<head>
<meta charset="utf-8">
<title>BrightPlacely.com – Contextual Advertising Network</title>
<link href="https://fonts.googleapis.com/css2?family=Source+Sans+3:wght@300;400;600;700&display=swap" rel="stylesheet">
<style>
:root{
  --lime:#9ab526;
  --lime-dark:#6f8a12;
  --lime-text:#8fb020;
  --grey-text:#6b6b6b;
  --grey-light:#8a8a8a;
  --rule:#c9c9c9;
  --white:#ffffff;
  --footer-head:#e4ee9e;
  --photo-top:#c9c9c9;
  --photo-bottom:#8d8d8d;
}
*{box-sizing:border-box;margin:0;padding:0}
html,body{width:900px;height:1200px;overflow:hidden;background:var(--white)}
body{font-family:"Source Sans 3",Arial,sans-serif;color:var(--grey-text);position:relative}
.page{position:relative;width:900px;height:1200px}

/* sidebar */
.sidebar{position:absolute;left:0;top:0;width:243px;height:1066px;border-left:1px solid var(--rule);border-right:1px solid var(--rule)}
.brand-mark{position:absolute;left:120px;top:26px;width:110px;text-align:center}
.brand-mark .dot{display:block;width:58px;height:58px;border-radius:50%;background:var(--lime);margin:0 auto 8px}
.brand-mark .name{font-size:14px;font-weight:600;color:var(--lime-text)}
.main-nav a{position:absolute;left:29px;width:188px;height:33px;background:var(--lime);border-radius:3px;color:var(--white);font-size:16px;text-decoration:none;line-height:33px;padding-left:34px;letter-spacing:.2px}
.side-tab{position:absolute;left:28px;width:189px;height:33px;border:1.5px solid var(--lime);border-radius:6px;background:var(--white);color:var(--lime-text);font-size:16px;line-height:30px;padding-left:11px;font-weight:300;letter-spacing:.2px}
.side-panel{position:absolute;left:30px;width:186px;border:1.5px solid var(--lime);border-top:none}
.register-now{position:absolute;left:28px;width:189px;height:60px;background:var(--lime);color:var(--white);font-size:22px;font-weight:300;text-align:center;line-height:58px;text-decoration:none}
.panel-copy{font-size:11px;font-weight:300;line-height:12px;letter-spacing:.3px;color:var(--grey-light);padding:14px 26px 0 12px}
.link-list{list-style:none;padding:10px 0 0 20px}
.link-list li{font-size:10.5px;font-weight:300;letter-spacing:.3px;line-height:17px;color:var(--grey-light)}
.link-list li::before{content:"* "}

/* header */
.search{position:absolute;left:557px;top:22px;width:323px;height:19px;background:var(--lime);border-radius:2px}
.search label{position:absolute;left:8px;top:3px;font-size:8px;color:var(--white)}
.search .field{position:absolute;left:41px;top:3px;width:277px;height:13px;background:var(--white)}
.search .drop{position:absolute;right:5px;top:4px;width:11px;height:11px;background:var(--lime-dark)}
.wordmark{position:absolute;left:270px;top:58px;font-size:36px;font-weight:700;color:var(--lime-text);letter-spacing:-.5px}

/* slider */
.slider{position:absolute;left:267px;top:129px;width:601px;height:350px;background:var(--lime);border-radius:6px}
.slide{position:absolute;left:3px;top:2px;width:595px;height:306px;border-radius:4px 4px 0 0;background:linear-gradient(180deg,var(--photo-top),var(--photo-bottom))}
.slider-dots{position:absolute;right:14px;top:318px;display:flex;gap:13px}
.slider-dots span{width:12px;height:12px;border-radius:50%;border:1.5px solid var(--white)}
.slider-dots .active{background:var(--white)}

/* intro */
.intro{position:absolute;left:273px;top:494px;width:594px;font-size:16px;font-weight:300;line-height:18.3px;letter-spacing:.45px;color:var(--grey-text)}
.intro p{text-align:justify;margin-bottom:5px}
.intro .plain{text-align:left;margin-bottom:0}
.intro strong{color:var(--lime-text);font-weight:600}
.features{list-style:none;margin:5px 0 3px}
.features li{height:23px;padding-left:21px;position:relative}
.features li::before{content:"";position:absolute;left:2px;top:5px;width:10px;height:8px;border:2px solid var(--lime);border-radius:50%}
.pull-quote{position:absolute;left:620px;top:612px;width:270px;font-size:28px;line-height:26px;letter-spacing:.6px;color:var(--lime-text);font-weight:300}
.pull-quote span{display:block;white-space:nowrap}

/* footer */
.site-footer{position:absolute;left:0;top:1066px;width:900px;height:134px;background:var(--lime);color:var(--white);font-size:9px;font-weight:300;letter-spacing:.2px;line-height:14px}
.site-footer h4{font-size:9px;font-weight:600;color:var(--footer-head)}
.footer-col{position:absolute;top:10px}
.pages-a{left:150px;width:66px;text-align:right}
.pages-b{left:227px;top:24px}
.useful{left:422px}
.pub{left:562px;width:140px;line-height:10px}
.pub h4{line-height:14px;margin-bottom:2px}
.neutral-badge{position:absolute;left:30px;top:22px;width:92px;height:52px;border:1.5px solid var(--white)}
.neutral-badge .shape{position:absolute;left:6px;top:6px;width:38px;height:38px;border-radius:50%;background:var(--white)}
.footer-emblem{position:absolute;left:774px;top:24px;width:44px;height:44px;border-radius:50%;background:var(--white)}
.copyright{position:absolute;left:715px;top:104px;font-size:9px}
</style>
</head>
<body>
<div class="page">

  <aside class="sidebar">
    <div class="brand-mark"><span class="dot"></span><span class="name">BrightPlacely</span></div>

    <nav class="main-nav">
      <a href="#" style="top:133px">ADVERTISERS</a>
      <a href="#" style="top:190px">PUBLISHERS</a>
      <a href="#" style="top:247px">REFERRAL</a>
      <a href="#" style="top:304px">OFFSETTING</a>
      <a href="#" style="top:361px">CONTACT</a>
    </nav>

    <div class="side-tab" style="top:429px">Advertiser Registration</div>
    <a href="#" class="register-now" style="top:462px">Registor Now!</a>
    <div class="side-panel" style="top:540px;height:158px">
      <p class="panel-copy" style="padding-top:30px">BrightPlacely.com can provide you access to over a billion impressions a month to drive quality traffic to your website to convert. Our advanced advertising technology enables a very high degree of targeting to improve the performance of your campaigns.</p>
    </div>
    <div class="side-tab" style="top:522px">Advertiser Registration</div>

    <div class="side-panel" style="top:712px;height:106px">
      <ul class="link-list" style="padding-top:26px">
        <li>Advertiser Information</li>
        <li>Advertiser Login</li>
        <li>Advertiser Sign Up</li>
        <li>Advertising Formats</li>
      </ul>
    </div>
    <div class="side-tab" style="top:696px">Advertisers</div>

    <div class="side-panel" style="top:832px;height:106px">
      <ul class="link-list" style="padding-top:26px">
        <li>Advertising Formats</li>
        <li>Publisher Information</li>
        <li>Publisher Login</li>
        <li>Publisher Sign Up</li>
      </ul>
    </div>
    <div class="side-tab" style="top:816px">Publishers</div>

    <div class="side-tab" style="top:952px">Publisher Registration</div>
    <a href="#" class="register-now" style="top:985px">Registor Now!</a>
  </aside>

  <div class="search"><label>Search</label><span class="field"></span><span class="drop"></span></div>
  <div class="wordmark">BrightPlacely.com</div>

  <section class="slider">
    <div class="slide" role="img" aria-label="Rotating header photo: a handshake between a gold-painted hand and a hand in a white shirt sleeve on a grey background"></div>
    <div class="slider-dots"><span></span><span></span><span class="active"></span><span></span><span></span></div>
  </section>

  <main class="intro">
    <p><strong>BrightPlacely.com</strong> is a contextual advertising network and ad exchange that brings together publishers of high quality content with advertisers, enabling them to reach their target market whilst publishers monetize their sites through advertising that's in keeping with their sites.</p>
    <p class="plain">Hundreds of millions of monthly ad impressions across ours and partner networks 170+ content channels to target</p>
    <ul class="features">
      <li>B2B &amp; B2C traffic</li>
      <li>Geo Targeting</li>
      <li>Behavioural Targeting</li>
      <li>Re-Targeting</li>
      <li>Real Time Campaign Tracking &amp; Reporting</li>
      <li>ROI tracking</li>
    </ul>
    <p style="margin-bottom:3px"><strong>BrightPlacely.com</strong> collates high quality content across a range of specialist and generalist websites and blogs quips advertisers with the tools to target visitors and optimize campaign</p>
    <p class="plain" style="margin-bottom:5px">performance.</p>
    <p>As you may have guested by our name BrightPlacely.com is both responsible and ethical.100% of the ads we serve are carbon offset meaning that you can feel good in the fact that the environmental impact of your advertising campaign has been neutrilized.</p>
  </main>

  <div class="pull-quote">
    <span style="padding-left:3px">ads we serve are</span>
    <span style="padding-left:40px;font-size:30px">carbon offset</span>
    <span style="font-size:30px">meaning that you</span>
    <span style="padding-left:67px">can feel good</span>
  </div>

  <footer class="site-footer">
    <div class="neutral-badge" role="img" aria-label="Carbon neutral website certificate"><span class="shape"></span></div>
    <div class="footer-col pages-a"><h4 style="padding-right:6px">Pages</h4>Contact<br>Offsetting<br>Referral<br>Publishers<br>Ad Formats</div>
    <div class="footer-col pages-b">Publisher Registration<br>Publisher Agreement<br>Advertisers<br>Ad Formats<br>Testimonials<br>Advertiser Registration<br>Advertiser Agreement</div>
    <div class="footer-col useful"><h4>Useful Info</h4>Contact us<br>Terms &amp; Conditions:<br>Advertisers<br>Terms &amp; Conditions:<br>Publishres<br>User Guide : Advertisers<br>User Guide : Publishers</div>
    <div class="footer-col pub"><h4>Publishers</h4>BrightPlacely.com offers publishers to the oppurtunity to earn more income through text (inlinks text links) or by displaying targeted contextual advertising banner ads on their websites or blogs.</div>
    <span class="footer-emblem"></span>
    <div class="copyright">Copyright BrightPlacely.com Ltd. 2010</div>
  </footer>

</div>
</body>
</html>
```